Chiropractic healthcare group business card

We are a Portland Oregon based chiropractic healthcare group. Looking for a new business card design. Something cutting edge, that shows off our new logo and tag line.Use either of the attached logos.Our tag line = "Who would you be without pain?"I'm open to about anything, impress me!!
Target Market(s)
Chiropractic patients - Auto injury, back pain, sports injuries, neck , shoulder, hip, knee, ankle pain.
Industry/Entity Type
Chiropractic
Contact Information for Business Card
Dr. Bram Holtvick, D.C.
Clinic name - Fernway Chiropractic
2 clinics
location #1
20418 NW Marwick Road
Suite B
North Plains, OR 97133
Location #2
13529 SE Calloway Street
Portland OR 97236
Main phone line 971.555.0143
website : www.FernwayClinics.example
Tag line "Who would you be without pain?"
Colors
Designer to choose colors to be used in the design.
Requirements
Must have
- Use the logo colors -- Want the orange color to be a TRUE orange.
- Both clinic address
- phone number
- website
- personal email - b.holtvick@ReliefBeginsHere.example
- tag line - "Who would you be without pain?"

```html
<!DOCTYPE html>
<html lang="en">
<head>
<meta charset="utf-8">
<title>Fernway Chiropractic – Stationery</title>
<link rel="stylesheet" href="https://fonts.googleapis.com/css2?family=Oswald:wght@300;400;500&display=swap">
<style>
  :root {
    --backdrop: #bccac9;
    --orange: #ff8306;
    --orange-deep: #e8700a;
    --orange-soft: #f59a45;
    --ink: #1e1e1e;
    --ink-soft: #3a3a3a;
    --paper: #ffffff;
    --bone: #eeeeee;
  }
  * { margin: 0; padding: 0; box-sizing: border-box; }
  html, body { width: 1200px; height: 859px; overflow: hidden; }
  body {
    background: var(--backdrop);
    font-family: "Oswald", "Arial Narrow", sans-serif;
    font-weight: 300;
    color: var(--ink);
    position: relative;
  }
  .piece { position: absolute; overflow: hidden; box-shadow: 1px 1px 2px rgba(0,0,0,.25); }
  .abs { position: absolute; }
  .wordmark {
    font-family: "Oswald", "Arial Narrow", sans-serif;
    font-weight: 500;
    color: var(--ink);
    text-transform: uppercase;
    text-align: center;
    line-height: 1.05;
    letter-spacing: .12em;
  }
  .icon { fill: var(--ink); }

  /* Card front */
  .card-front { left: 56px; top: 65px; width: 233px; height: 149px; }
  .card-front .photo {
    inset: 0;
    background:
      radial-gradient(ellipse 60% 80% at 75% 55%, #f7b878 0%, rgba(247,184,120,0) 70%),
      radial-gradient(ellipse 40% 40% at 35% 10%, #f4a35a 0%, rgba(244,163,90,0) 70%),
      linear-gradient(160deg, var(--orange-deep) 0%, var(--orange) 55%, #d9680c 100%);
  }
  .card-front .logo-panel {
    left: 0; top: 58px; width: 113px; height: 55px;
    background: var(--paper);
    display: flex; align-items: center; justify-content: center;
  }
  .card-front .logo-panel .wordmark { font-size: 11px; padding-top: 6px; }
  .card-front .ribbon {
    left: 7px; top: 55px; width: 98px; height: 8px;
    background: var(--orange);
    color: var(--paper);
    font-style: italic; font-size: 4.6px; letter-spacing: .06em;
    display: flex; align-items: center; justify-content: center;
  }
  .card-front .web {
    left: 0; top: 114px; width: 113px;
    text-align: center; color: var(--paper);
    font-size: 4.3px; font-weight: 400; letter-spacing: .02em;
  }

  /* Card back */
  .card-back { left: 56px; top: 242px; width: 233px; height: 149px; background: var(--paper); }
  .card-back .spine {
    left: 0; top: 0; width: 70px; height: 149px;
    background: linear-gradient(90deg, #e9e9e9 0%, #f3f3f3 55%, rgba(255,255,255,0) 100%);
  }
  .band { background: var(--orange); }
  .card-back .band-left { left: 0; top: 12px; width: 46px; height: 16px; }
  .card-back .band-right {
    left: 93px; top: 12px; width: 140px; height: 16px;
    color: var(--paper); font-style: italic; font-size: 5.6px; letter-spacing: .06em;
    display: flex; align-items: center; justify-content: center;
  }
  .card-back .logo-slot { left: 46px; top: 6px; width: 47px; height: 26px; display: flex; align-items: center; justify-content: center; }
  .card-back .logo-slot .wordmark { font-size: 6px; letter-spacing: .08em; }
  .card-back .contact-row {
    left: 74px; top: 40px; width: 140px; height: 10px;
    display: flex; align-items: center; font-size: 5.4px; font-weight: 400; letter-spacing: .03em; white-space: nowrap;
  }
  .contact-row svg { width: 6px; height: 6px; margin-right: 3px; flex: none; }
  .card-back .row-divider { width: .6px; height: 10px; background: var(--orange); margin: 0 4px; }
  .card-back .rule { left: 74px; top: 55px; width: 140px; height: .6px; background: var(--orange); }
  .card-back .col-divider { left: 150px; top: 59px; width: .6px; height: 42px; background: var(--orange); }
  .card-back .clinic {
    top: 60px; width: 66px; text-align: center; font-size: 5.1px; line-height: 1.4; font-weight: 400;
  }
  .card-back .clinic svg { width: 9px; height: 12px; display: block; margin: 0 auto 4px; }
  .card-back .clinic-one { left: 81px; }
  .card-back .clinic-two { left: 145px; }
  .card-back .name {
    left: 74px; top: 109px; width: 152px; text-align: center;
    color: var(--orange); font-weight: 400; font-size: 12px; letter-spacing: .02em;
  }
  .card-back .title {
    left: 74px; top: 126px; width: 152px; text-align: center; font-size: 6.4px; font-weight: 400;
  }

  /* Letterhead */
  .letterhead { left: 330px; top: 66px; width: 515px; height: 728px; background: var(--paper); }
  .letterhead .spine {
    left: 0; top: 240px; width: 190px; height: 488px;
    background: linear-gradient(90deg, #ececec 0%, #f1f1f1 50%, rgba(255,255,255,0) 100%);
  }
  .letterhead .band-left { left: 0; top: 30px; width: 62px; height: 40px; }
  .letterhead .band-right {
    left: 171px; top: 30px; width: 344px; height: 40px;
    color: var(--paper); font-style: italic; font-size: 15px; letter-spacing: .06em;
    display: flex; align-items: center; justify-content: center;
  }
  .letterhead .logo-slot { left: 62px; top: 22px; width: 109px; height: 58px; display: flex; align-items: center; justify-content: center; }
  .letterhead .logo-slot .wordmark { font-size: 14px; }
  .letterhead .footer {
    left: 36px; top: 670px; width: 450px; height: 34px;
    display: flex; font-size: 10.5px; font-weight: 300; letter-spacing: .03em; line-height: 15px;
  }
  .letterhead .footer .col { display: flex; flex-direction: column; }
  .letterhead .footer .line { display: flex; align-items: center; white-space: nowrap; }
  .letterhead .footer svg { width: 10px; height: 10px; margin-right: 6px; flex: none; }
  .letterhead .footer .address { text-align: center; display: block; }
  .letterhead .footer .divider { width: .8px; height: 30px; background: var(--orange); margin: 0 12px; }

  /* Envelope */
  .envelope { left: 878px; top: 256px; width: 270px; height: 538px; background: var(--orange); }
  .envelope .spine {
    left: 0; top: 9px; width: 270px; height: 180px;
    background: linear-gradient(170deg, #f29333 0%, #f7a24e 40%, #f08b20 75%, rgba(255,131,6,0) 100%);
  }
  .envelope .logo-panel {
    left: 0; top: 43px; width: 66px; height: 88px; background: var(--paper);
    display: flex; align-items: center; justify-content: center;
  }
  .envelope .logo-panel .wordmark { transform: rotate(-90deg); font-size: 10px; white-space: nowrap; }
</style>
</head>
<body>

<svg width="0" height="0" style="position:absolute">
  <defs>
    <symbol id="i-phone" viewBox="0 0 24 24"><path d="M6.6 2.5 9.4 6c.4.5.3 1.2-.1 1.6L7.6 9.2c1.4 2.9 3.9 5.4 7.2 7.2l1.6-1.7c.4-.4 1.1-.5 1.6-.1l3.5 2.8c.5.4.6 1.2.1 1.7l-2 2.1c-.7.7-1.8 1-2.8.6C9.6 19.6 4.4 14.4 2.2 7.2c-.3-1 0-2.1.7-2.8l2-2c.5-.5 1.3-.4 1.7.1z" fill="none" stroke="#1e1e1e" stroke-width="1.8"/></symbol>
    <symbol id="i-mail" viewBox="0 0 24 24"><path d="M2 5h20v14H2z"/><path d="M2 5l10 8 10-8" fill="none" stroke="#fff" stroke-width="1.6"/></symbol>
    <symbol id="i-pin" viewBox="0 0 18 24"><path d="M9 0C4 0 0 4 0 9c0 6.5 9 15 9 15s9-8.5 9-15c0-5-4-9-9-9zm0 13a4 4 0 1 1 0-8 4 4 0 0 1 0 8z"/></symbol>
  </defs>
</svg>

<!-- Business card, front -->
<section class="piece card-front" aria-label="Business card front">
  <div class="abs photo" role="img" aria-label="Orange-toned photo of a neck with the cervical spine shown"></div>
  <div class="abs logo-panel"><span class="wordmark">Fernway<br>Chiropractic</span></div>
  <div class="abs ribbon">Who would you be without pain?</div>
  <p class="abs web">www.FernwayClinics.example</p>
</section>

<!-- Business card, back -->
<section class="piece card-back" aria-label="Business card back">
  <div class="abs spine" role="img" aria-label="Faint white rendering of vertebrae"></div>
  <div class="abs band band-left"></div>
  <div class="abs logo-slot"><span class="wordmark">Fernway</span></div>
  <div class="abs band band-right">Who would you be WITHOUT PAIN?</div>
  <div class="abs contact-row">
    <svg class="icon"><use href="#i-phone"/></svg>971.555.0143
    <span class="row-divider"></span>
    <svg class="icon"><use href="#i-mail"/></svg>b.holtvick@ReliefBeginsHere.example
  </div>
  <div class="abs rule"></div>
  <div class="abs col-divider"></div>
  <div class="abs clinic clinic-one">
    <svg class="icon" viewBox="0 0 18 24"><use href="#i-pin"/></svg>
    20418 NW Marwick Road<br>Suite B, North Plains,<br>OR 97133
  </div>
  <div class="abs clinic clinic-two">
    <svg class="icon" viewBox="0 0 18 24"><use href="#i-pin"/></svg>
    13529 SE<br>Calloway Street<br>Portland OR 97236
  </div>
  <h1 class="abs name">DR. BRAM HOLTVICK, D.C.</h1>
  <p class="abs title">Chiropractor | Fernway Chiropractic</p>
</section>

<!-- Letterhead -->
<section class="piece letterhead" aria-label="Letterhead">
  <div class="abs spine" role="img" aria-label="Faint white rendering of a spinal column"></div>
  <div class="abs band band-left"></div>
  <div class="abs logo-slot"><span class="wordmark">Fernway<br>Chiropractic</span></div>
  <div class="abs band band-right">Who would you be WITHOUT PAIN?</div>
  <footer class="abs footer">
    <div class="col">
      <span class="line"><svg class="icon"><use href="#i-phone"/></svg>971.555.0143</span>
      <span class="line"><svg class="icon"><use href="#i-mail"/></svg>b.holtvick@ReliefBeginsHere.example</span>
    </div>
    <span class="divider"></span>
    <div class="col">
      <span class="line"><svg class="icon" viewBox="0 0 18 24"><use href="#i-pin"/></svg>20418 NW Marwick Road, Suite B,</span>
      <span class="address">North Plains, OR 97133</span>
    </div>
    <span class="divider"></span>
    <div class="col">
      <span class="line"><svg class="icon" viewBox="0 0 18 24"><use href="#i-pin"/></svg>13529 SE Calloway Street</span>
      <span class="address">Portland OR 97236</span>
    </div>
  </footer>
</section>

<!-- Envelope -->
<section class="piece envelope" aria-label="Envelope">
  <div class="abs spine" role="img" aria-label="Orange-toned rendering of vertebrae across the top"></div>
  <div class="abs logo-panel"><span class="wordmark">Fernway Chiropractic</span></div>
</section>

</body>
</html>
```